Design my New and Engaging Wix Website

We just recently started a new website for Harbor Lumen (www.harbor-lumen.example) and would like to have a custom design for it. The design should be engaging and modern. You can use our logo and design the website inspired by the style.

```html
<!DOCTYPE html>
<html lang="en">
<head>
<meta charset="utf-8">
<title>Harbor Lumen — Peace Learning</title>
<link href="https://fonts.googleapis.com/css2?family=Merriweather:wght@700;900&family=Lato:wght@400;700&display=swap" rel="stylesheet">
<style>
:root{
  --blue:#0b8fe0;
  --blue-dark:#0677c4;
  --navy:#0c0f2e;
  --ink:#222;
  --muted:#444;
  --field:#f3f3f3;
  --green:#5b8a2f;
  --footer:#141414;
  --white:#fff;
}
*{margin:0;padding:0;box-sizing:border-box}
html,body{width:1200px;height:3955px;overflow:hidden}
body{font-family:'Lato',sans-serif;color:var(--ink);background:var(--white);position:relative}
.serif{font-family:'Merriweather',serif}
section,header,footer{position:absolute;left:0;width:1200px}
.abs{position:absolute}
.btn{position:absolute;display:flex;align-items:center;justify-content:space-between;background:var(--blue);color:var(--white);border-radius:20px;font-family:'Merriweather',serif;font-weight:700;font-size:15px;padding:0 6px 0 15px;box-shadow:0 0 0 2px rgba(255,255,255,.9)}
.btn svg{width:26px;height:26px}
.center{text-align:center;width:1200px;left:0}

/* hero */
.hero{top:0;height:588px;background:radial-gradient(ellipse at 68% 45%,#4a4fb0 0%,#20236a 30%,var(--navy) 70%)}
.brand{position:absolute;display:flex;align-items:center;gap:10px;font-family:'Lato',sans-serif;font-weight:700;color:var(--white)}
.brand i{display:block;border-radius:50%;border:2px solid var(--white)}
.nav{position:absolute;top:24px;left:417px;display:flex;gap:36px;color:var(--white);font-size:15px}
.hero h1{position:absolute;left:110px;top:196px;color:var(--white);font-size:39px;line-height:51px;font-weight:700}
.hero p{position:absolute;left:110px;top:303px;width:560px;color:var(--white);font-size:15px;line-height:28px}
.dots{position:absolute;top:532px;left:1014px;display:flex;gap:12px}
.dots span{width:14px;height:14px;border-radius:50%;background:var(--white)}
.dots span.on{background:var(--blue)}

/* about */
.about{top:588px;height:528px}
.h2{color:var(--blue);font-family:'Merriweather',serif;font-weight:700;font-size:30px}
.about .h2{position:absolute;left:598px;top:100px}
.about p{position:absolute;left:598px;top:142px;width:490px;font-size:14.5px;line-height:28.2px;color:var(--muted)}

/* what we do */
.wwd{top:1116px;height:523px;background:linear-gradient(135deg,#0c93e4,#0a86d6 60%,#1b98e6)}
.wwd h2{position:absolute;top:60px;color:var(--white);font-size:36px}
.svc{position:absolute;top:165px;width:300px;text-align:center;color:var(--white)}
.svc svg{display:block;margin:0 auto}
.svc h3{font-family:'Merriweather',serif;font-size:19px;line-height:29px;margin-top:12px}
.svc p{font-size:14.5px;line-height:26px;margin-top:4px;opacity:.95}

/* video */
.video{top:1639px;height:823px}
.video .h2{position:absolute;top:78px}
.video p{position:absolute;top:124px;left:190px;width:820px;text-align:center;font-size:14.5px;line-height:28px;color:var(--muted)}
.video .frame{position:absolute;left:146px;top:229px;width:910px;height:505px;background:var(--green)}

/* consortium */
.consort{top:2462px;height:454px;background:radial-gradient(ellipse at 30% 60%,#2aa2ee,#0a88d8 60%,#0778c6)}
.consort h2{position:absolute;top:50px;color:var(--white);font-size:30px}
.card{position:absolute;top:139px;width:471px;height:223px;background:var(--white);display:flex}
.card .photo{width:176px;height:223px;flex:none}
.card .body{padding:18px 12px 0 24px}
.card h3{color:var(--blue);font-family:'Merriweather',serif;font-size:18px;line-height:26px}
.card p{font-size:14px;line-height:27px;color:var(--muted);margin-top:2px}
.card .meta{font-family:'Merriweather',serif;font-weight:700;font-size:14px;margin-top:2px;display:flex;gap:14px;align-items:center}
.card .meta span{display:flex;gap:5px;align-items:center}
.card .more{color:var(--blue);font-family:'Merriweather',serif;font-weight:700;font-size:14px;margin-top:6px}

/* contact */
.contact{top:2916px;height:678px}
.contact .eyebrow{position:absolute;top:84px;font-family:'Merriweather',serif;font-weight:700;font-size:17px}
.contact .h2{position:absolute;top:118px}
.contact p.lead{position:absolute;top:164px;left:190px;width:820px;text-align:center;font-size:14.5px;line-height:28px;color:var(--muted)}
.info{position:absolute;top:246px;height:46px;background:var(--field);border-left:3px solid var(--blue);display:flex;align-items:center;gap:6px;padding:0 10px;font-family:'Merriweather',serif;font-weight:700;font-size:14px}
.field{position:absolute;background:var(--field);box-shadow:0 2px 4px rgba(0,0,0,.08);display:flex;align-items:center;gap:8px;padding:0 12px;font-size:14.5px;color:#555}
.field .sep{width:1px;height:18px;background:#555}
.field.msg{align-items:flex-start;padding-top:16px}

/* footer */
.foot{top:3594px;height:361px;background:var(--footer);color:var(--white)}
.foot h4{font-family:'Merriweather',serif;font-size:18px;position:absolute;top:62px}
.foot ul{list-style:none;position:absolute;top:92px;font-size:14.5px;line-height:26px}
.foot .about-text{position:absolute;left:112px;top:140px;width:290px;font-size:14.5px;line-height:28px}
.social{position:absolute;left:114px;top:266px;display:flex;gap:10px}
.social span{width:30px;height:30px;border-radius:50%;background:var(--blue);border:2px solid var(--white)}
.fcontact{position:absolute;left:843px;font-size:14.5px;display:flex;gap:10px;align-items:center}
.copy{position:absolute;top:303px;font-size:14.5px}
</style>
</head>
<body>

<header class="hero">
  <div role="img" aria-label="Photo: a hand touching a glowing digital network" class="abs" style="left:560px;top:0;width:640px;height:588px;background:radial-gradient(ellipse at 60% 40%,rgba(120,110,230,.55),rgba(12,15,46,0) 65%)"></div>
  <div class="brand" style="left:112px;top:20px;font-size:24px"><i style="width:22px;height:22px"></i>Harbor Lumen</div>
  <nav class="nav"><span>Home</span><span>About Us</span><span>What We do</span><span>Project</span><span>Doner</span><span>Contact Us</span></nav>
  <div class="btn" style="left:982px;top:17px;width:106px;height:34px">Log In
    <svg viewBox="0 0 26 26"><circle cx="13" cy="13" r="12" fill="#fff"/><circle cx="13" cy="10" r="3.5" fill="#0b8fe0"/><path d="M7 19c1-4 11-4 12 0z" fill="#0b8fe0"/></svg></div>
  <h1 class="serif">QUALITATIVE AND ACCESSIBLE<br>PEACE EDUCATION RESOURCES</h1>
  <p>Lorem ipsum dolor sit amet, consectetur adipiscing elit, sed do eiusmod tempor dolore magna aliqua. Ut enim ad minim veniam, quis nostrud exercitation</p>
  <div class="btn" style="left:112px;top:373px;width:138px;height:34px">Get Started
    <svg viewBox="0 0 26 26"><circle cx="13" cy="13" r="12" fill="#fff"/><path d="M8 13h9M13 9l4 4-4 4" stroke="#0b8fe0" stroke-width="2.4" fill="none" stroke-linecap="round"/></svg></div>
  <div class="dots"><span></span><span class="on"></span><span></span></div>
</header>

<section class="about">
  <svg class="abs" style="left:100px;top:85px" width="430" height="360" viewBox="0 0 430 360">
    <path d="M330 150 L425 250 L340 250 Z" fill="#0b8fe0"/>
    <circle cx="185" cy="180" r="176" fill="#0b8fe0"/>
  </svg>
  <div role="img" aria-label="Photo: a person touching a floating network of cloud icons" class="abs" style="left:127px;top:107px;width:316px;height:316px;border-radius:50%;background:radial-gradient(circle at 45% 50%,#6a6460,#2c2a2a 55%,#4a4d52)"></div>
  <h2 class="h2">ABOUT US</h2>
  <p>In an increasingly internationalized world, complex and manifold conflicts arise between individuals, groups, organizations, and states. To find ways of dealing with these issues in a constructive and peaceful manner is a central challenge for modern societies. Harbor Lumen aims to empower communities affected by unresolved conflicts and strengthen their capacities to address them effectivelyWithin our pilot project "Open Bridges for Peace Learning in Ukraine" the Northvale University (NVU) in</p>
  <div class="btn" style="left:598px;top:385px;width:136px;height:34px">Read More
    <svg viewBox="0 0 26 26"><circle cx="13" cy="13" r="12" fill="#fff"/><path d="M8 13h9M13 9l4 4-4 4" stroke="#0b8fe0" stroke-width="2.4" fill="none" stroke-linecap="round"/></svg></div>
</section>

<section class="wwd">
  <h2 class="serif center">WHAT WE DO</h2>
  <div class="svc" style="left:123px">
    <svg width="200" height="140" viewBox="0 0 200 140"><path d="M80 70 L32 138 L120 128Z" fill="#fff"/><circle cx="150" cy="79" r="77" fill="#fff"/><circle cx="150" cy="79" r="59" fill="#0b8fe0"/>
      <g stroke="#fff" stroke-width="3" fill="none"><path d="M120 62l30-14 30 14-30 14z"/><path d="M130 67v12c12 7 28 7 40 0V67"/><rect x="124" y="86" width="52" height="8" rx="2"/><rect x="128" y="96" width="48" height="8" rx="2"/><rect x="124" y="106" width="52" height="8" rx="2"/></g></svg>
    <h3>Developing peace<br>Education curricular</h3>
    <p>Modernizing and internationalizing higher education</p>
  </div>
  <div class="svc" style="left:453px">
    <svg width="200" height="140" viewBox="0 0 200 140"><path d="M80 70 L32 138 L120 128Z" fill="#fff"/><circle cx="150" cy="79" r="77" fill="#fff"/><circle cx="150" cy="79" r="59" fill="#0b8fe0"/>
      <g stroke="#fff" stroke-width="3" fill="none"><rect x="122" y="52" width="56" height="32" rx="3"/><circle cx="130" cy="100" r="4"/><circle cx="150" cy="100" r="4"/><circle cx="170" cy="100" r="4"/><path d="M123 114c0-6 14-6 14 0M143 114c0-6 14-6 14 0M163 114c0-6 14-6 14 0M132 68h16"/><circle cx="164" cy="66" r="6"/></g></svg>
    <h3>Teaching And<br>Training</h3>
    <p>Utilizing the potential of hybrid learning</p>
  </div>
  <div class="svc" style="left:780px">
    <svg width="200" height="140" viewBox="0 0 200 140"><path d="M80 70 L32 138 L120 128Z" fill="#fff"/><circle cx="150" cy="79" r="77" fill="#fff"/><circle cx="150" cy="79" r="59" fill="#0b8fe0"/>
      <g stroke="#fff" stroke-width="3" fill="none"><rect x="128" y="50" width="22" height="30" rx="2"/><path d="M134 60h10M134 68h10"/><rect x="124" y="84" width="40" height="26" rx="2"/><circle cx="158" cy="96" r="7"/><path d="M160 72l18 14-10 14"/></g></svg>
    <h3>Producing Peace<br>Education Resources</h3>
    <p>Providing engaging and high quality content</p>
  </div>
</section>

<section class="video">
  <h2 class="h2 center">OUR VIDEO</h2>
  <p>Lorem ipsum dolor sit amet, consectetur adipiscing elit, sed do eiusmod tempor incididunt ut labore et dolore magna aliqua. Ut enim ad minim veniam, quis nostrud exercitation ullamco laboris nisi ut</p>
  <div class="frame" role="img" aria-label="Video thumbnail: illustrated globe with groups of people in dialogue"></div>
  <svg class="abs" style="left:556px;top:2104px" width="84" height="84" viewBox="0 0 84 84"><circle cx="42" cy="42" r="41" fill="#7fc4f0"/><circle cx="42" cy="42" r="33" fill="#0b8fe0"/><path d="M35 28l20 14-20 14z" fill="#fff"/></svg>
</section>

<section class="consort">
  <h2 class="serif center">PROJECT CONSORTIUM</h2>
  <article class="card" style="left:112px">
    <div class="photo" role="img" aria-label="Photo: library shelves full of books" style="background:linear-gradient(90deg,#6b3f24,#b88a5c 50%,#5a3a26)"></div>
    <div class="body">
      <h3>Northvale University<br>Centre</h3>
      <p>Lorem ipsum dolor sit consectetur adipiscing elit, sed do eiusmod tempor incididunt ut labore et dolore</p>
      <div class="meta"><span>By Lorem ipsum</span><span><svg width="14" height="14" viewBox="0 0 14 14"><rect x="1" y="2" width="12" height="11" fill="none" stroke="#0b8fe0" stroke-width="1.6"/><path d="M1 5h12" stroke="#0b8fe0" stroke-width="1.6"/></svg>08.12.2021</span></div>
      <div class="more">Read More ›</div>
    </div>
  </article>
  <article class="card" style="left:617px">
    <div class="photo" role="img" aria-label="Photo: students talking together at a table" style="background:linear-gradient(135deg,#cfd6dc,#8b8f94 55%,#4c4f55)"></div>
    <div class="body">
      <h3>Northvale University<br>Centre</h3>
      <p>Lorem ipsum dolor sit consectetur adipiscing elit, sed do eiusmod tempor incididunt ut labore et dolore</p>
      <div class="meta"><span>By Lorem ipsum</span><span><svg width="14" height="14" viewBox="0 0 14 14"><rect x="1" y="2" width="12" height="11" fill="none" stroke="#0b8fe0" stroke-width="1.6"/><path d="M1 5h12" stroke="#0b8fe0" stroke-width="1.6"/></svg>08.12.2021</span></div>
      <div class="more">Read More ›</div>
    </div>
  </article>
</section>

<section class="contact">
  <div class="eyebrow center">CONTACT US</div>
  <h2 class="h2 center">GET IN TOUCH</h2>
  <p class="lead">Lorem ipsum dolor sit amet, consectetur adipiscing elit, sed do eiusmod tempor incididunt ut labore et dolore magna aliqua. Ut enim ad minim veniam, quis nostrud exercitation ullamco laboris nisi ut aliquip ex ea</p>
  <div class="info" style="left:437px;width:159px"><svg width="14" height="14" viewBox="0 0 14 14"><path d="M3 1l3 3-2 2c1 2 2 3 4 4l2-2 3 3-2 2C6 13 1 8 1 3z" fill="#222"/></svg>: 123 456 7890</div>
  <div class="info" style="left:611px;width:265px"><svg width="15" height="12" viewBox="0 0 15 12"><rect x="1" y="1" width="13" height="10" fill="none" stroke="#222" stroke-width="1.5"/><path d="M1 1l6.5 5L14 1" fill="none" stroke="#222" stroke-width="1.5"/></svg>: mara.olsen@northvale.example</div>
  <div class="field" style="left:256px;top:314px;width:332px;height:44px"><svg width="12" height="13" viewBox="0 0 12 13"><circle cx="6" cy="4" r="3.5" fill="#333"/><path d="M0 13c0-5 12-5 12 0z" fill="#333"/></svg><span class="sep"></span>Frist Name</div>
  <div class="field" style="left:612px;top:314px;width:332px;height:44px"><svg width="12" height="13" viewBox="0 0 12 13"><circle cx="6" cy="4" r="3.5" fill="#333"/><path d="M0 13c0-5 12-5 12 0z" fill="#333"/></svg><span class="sep"></span>Last Name</div>
  <div class="field" style="left:256px;top:371px;width:332px;height:43px"><svg width="13" height="13" viewBox="0 0 14 14"><path d="M3 1l3 3-2 2c1 2 2 3 4 4l2-2 3 3-2 2C6 13 1 8 1 3z" fill="none" stroke="#333" stroke-width="1.3"/></svg><span class="sep"></span>Phone</div>
  <div class="field" style="left:612px;top:371px;width:332px;height:43px"><svg width="15" height="12" viewBox="0 0 15 12"><rect x="1" y="1" width="13" height="10" fill="none" stroke="#333" stroke-width="1.4"/><path d="M1 1l6.5 5L14 1" fill="none" stroke="#333" stroke-width="1.4"/></svg><span class="sep"></span>Emai Address</div>
  <div class="field msg" style="left:256px;top:429px;width:683px;height:102px"><svg width="15" height="12" viewBox="0 0 15 12"><rect x="0" y="0" width="15" height="12" fill="#333"/><path d="M0 0l7.5 6L15 0" fill="none" stroke="#f3f3f3" stroke-width="1.4"/></svg><span class="sep"></span>Message</div>
  <div class="btn" style="left:545px;top:563px;width:110px;height:34px">Submit
    <svg viewBox="0 0 26 26"><circle cx="13" cy="13" r="12" fill="#fff"/><path d="M8 13h9M13 9l4 4-4 4" stroke="#0b8fe0" stroke-width="2.4" fill="none" stroke-linecap="round"/></svg></div>
</section>

<footer class="foot">
  <svg class="abs" style="left:0;top:-10px" width="1200" height="12" viewBox="0 0 1200 12"><path d="M700 12 Q890 -4 1110 12Z" fill="#cfe6f7"/></svg>
  <div class="brand" style="left:112px;top:72px;font-size:34px;color:var(--blue)"><i style="width:28px;height:28px;border-color:var(--blue)"></i>Harbor Lumen</div>
  <p class="about-text">Lorem ipsum dolor sit amet, consectetur adipiscing elit, sed do eiusmod tempor incididunt ut labore et dolore magna aliqua. Ut enim ad minim veniam, quis</p>
  <div class="social"><span></span><span></span><span></span><span></span></div>
  <h4 style="left:454px">Using Links</h4>
  <ul style="left:454px"><li>Home</li><li>About Us</li><li>What We do</li><li>project</li><li>Doner</li><li>Contact Us</li></ul>
  <h4 style="left:657px">HELP Links</h4>
  <ul style="left:657px"><li>Terms&amp;condtions</li><li>Privacy Policy</li><li>Latest News</li><li>Support</li></ul>
  <h4 style="left:843px;top:58px">Contact Us</h4>
  <div class="fcontact" style="top:88px"><svg width="13" height="13" viewBox="0 0 14 14"><path d="M3 1l3 3-2 2c1 2 2 3 4 4l2-2 3 3-2 2C6 13 1 8 1 3z" fill="#fff"/></svg>123 456 7890</div>
  <div class="fcontact" style="top:120px"><svg width="14" height="11" viewBox="0 0 15 12"><rect x="1" y="1" width="13" height="10" fill="none" stroke="#fff" stroke-width="1.5"/><path d="M1 1l6.5 5L14 1" fill="none" stroke="#fff" stroke-width="1.5"/></svg>mara.olsen@northvale.example</div>
  <div class="fcontact" style="top:160px"><svg width="12" height="15" viewBox="0 0 12 15"><path d="M6 15C2 10 0 7 0 5a6 6 0 0112 0c0 2-2 5-6 10z" fill="#fff"/><circle cx="6" cy="5" r="2" fill="#141414"/></svg>&nbsp;Lorem ipsum</div>
  <div class="fcontact" style="top:192px;left:865px">58,dolor sit amet,</div>
  <div class="copy center">©Copyrights 2021 &nbsp; Harbor Lumen | All Rights Reserved</div>
</footer>

</body>
</html>
```